Very High End Grooming Salon needs new business card design

I need a very nice card design I am a certified Master groomer we have a very high end clients. Our color is pink but does not have to be pink. I have a logo also a mission statement .
Fluff N Fern Pet Boutique and Spa
48810 Marlow Rd
Seabrook Cove fl 33471
555 904 3782
www.fluffernboutique.example
online booking available
this is our mission statement not sure it need to go on card but here it is.
Our Mission is to show respect to all animals pampering them with the same high end tailored service one would expect to receive at a day spa
as the only certified master groomer in the area we strive to put your pets best paw forward.

Industry/Entity Type

Business

```html
<!DOCTYPE html>
<html lang="en">
<head>
<meta charset="utf-8">
<title>Fluff N Fern Pet Boutique and Spa – Business Card</title>
<link rel="stylesheet" href="https://fonts.googleapis.com/css2?family=Great+Vibes&family=Tinos&display=swap">
<style>
  :root {
    --card-white: #ffffff;
    --header-grey: #e5e7e8;
    --brand-pink: #e0049c;
    --script-pink: #d6339f;
    --logo-pink: #f18fd6;
    --ink: #141414;
    --paw-grey: #3d3f3f;
  }
  * { margin: 0; padding: 0; box-sizing: border-box; }
  html, body {
    width: 1200px;
    height: 744px;
    overflow: hidden;
    background: var(--card-white);
  }
  .business-card {
    position: relative;
    width: 1200px;
    height: 744px;
    background: var(--card-white);
    font-family: "Tinos", "Times New Roman", serif;
    color: var(--ink);
  }
  .header-panel {
    position: absolute;
    left: 19px;
    top: 11px;
    width: 1138px;
    height: 342px;
    background: var(--header-grey);
  }
  .accent-band {
    position: absolute;
    left: 19px;
    top: 353px;
    width: 1138px;
    height: 35px;
    background: var(--brand-pink);
  }
  .brand-mark {
    position: absolute;
    left: 72px;
    top: 28px;
    width: 222px;
    height: 320px;
    display: flex;
    flex-direction: column;
    align-items: center;
    justify-content: center;
    gap: 22px;
  }
  .brand-mark-dot {
    width: 130px;
    height: 130px;
    border-radius: 50%;
    background: var(--logo-pink);
  }
  .brand-mark-name {
    font-size: 30px;
    color: var(--script-pink);
    white-space: nowrap;
  }
  .business-name {
    position: absolute;
    left: 328px;
    top: 56px;
    font-family: "Great Vibes", cursive;
    font-size: 51px;
    font-weight: 400;
    line-height: 1;
    color: var(--script-pink);
    white-space: nowrap;
  }
  .owner {
    position: absolute;
    left: 419px;
    top: 134px;
    font-size: 32px;
    line-height: 44px;
  }
  .address {
    position: absolute;
    left: 46px;
    top: 506px;
    font-size: 24px;
    line-height: 34px;
    font-style: normal;
  }
  .phone {
    position: absolute;
    left: 538px;
    top: 536px;
    font-size: 30px;
    line-height: 1.2;
    word-spacing: 2px;
  }
  .paw-prints {
    position: absolute;
    left: 911px;
    top: 595px;
    width: 158px;
    height: 83px;
    border-radius: 40px;
    background: var(--paw-grey);
  }
</style>
</head>
<body>
  <main class="business-card">
    <div class="header-panel"></div>
    <div class="accent-band"></div>

    <div class="brand-mark">
      <span class="brand-mark-dot"></span>
      <span class="brand-mark-name">Fluff N Fern</span>
    </div>

    <h1 class="business-name">Fluff N Fern Pet Boutique and Spa</h1>

    <p class="owner">Mara Ellison<br>Owner</p>

    <address class="address">
      48810 Marlow Rd<br>
      Seabrook Cove fl 33471
    </address>

    <p class="phone">Phone :&nbsp; 555 904 3782</p>

    <div class="paw-prints" role="img" aria-label="Two dark grey paw print illustrations"></div>
  </main>
</body>
</html>
```